Business Card Design Project

I need a business card design for a new business called Thornal Insurance Services. I am a small insurance broker that will provide business insurance services mostly to contractors and small businesses. My business is all about customer service and assistance rather than being a price driven/focused business. I want my business card to be professional giving the impression that I am larger than one person but not a corporate company. I have attached a copy of my logo.
Updates

Hi all

I have been advised that I need to show the following info for compliance reasons on my card. It only has to be small.

Can you please include either front or back:

Thornal Insurance Services Pty Ltd [ABN 61728405913] AR No 586027 as Authorised Representative of Carrodine Insurance Group Pty Ltd ACN 274 619 508 ABN 82 274 619 508 AFS Licence No 718246

Reason: I need a further change to be made to the design. I need the contact number of 1300584619 added to the business card.

Hi All

I need one last change made to the card.

Can you please include the phone number 1300584619 to the card. If possible can this be made fairly clear on the card, either large on the back or another design idea you may have.

Target Market(s)

30+ Professionals

Industry/Entity Type

Insurance

Requirements
Must have
• I want a double sided design. My details to go on the card are as follows:

Dean Thornal QRTMOL (Snr Assoc.) CIP
Director
PO Box 782, Fernmoor SA 5071
Phone: 0438 612 704
Fax 08 8347 2910
Email: dean@thornalcover.example.au
Website: http://www.thornalcover.example.au
Twitter: Thornalcover
Facebook: facebook.com/thornalcover

```html
<!DOCTYPE html>
<html lang="en">
<head>
<meta charset="utf-8">
<title>Thornal Insurance Services – Business Card</title>
<link rel="stylesheet" href="https://fonts.googleapis.com/css2?family=Didact+Gothic&family=Arimo:wght@700&display=swap">
<style>
  :root {
    --page-bg: #e6e6e6;
    --card-dark: #1c1c1c;
    --card-dark-mid: #3a3a3a;
    --card-light: #ffffff;
    --ink: #2a2a2a;
    --ink-soft: #555555;
    --accent-red: #e01f26;
    --muted-grey: #8a8a8a;
    --tab-black: #111111;
    --twitter-blue: #3fa9e0;
    --facebook-blue: #3b5b99;
  }
  * { box-sizing: border-box; margin: 0; padding: 0; }
  html, body {
    width: 1200px; height: 900px; overflow: hidden;
    background: var(--page-bg);
    font-family: "Didact Gothic", "Century Gothic", sans-serif;
  }
  .sheet {
    width: 1200px; height: 900px;
    display: flex; align-items: center; justify-content: center; gap: 40px;
  }
  .card {
    position: relative;
    width: 540px; height: 330px;
    border-radius: 18px;
    overflow: hidden;
    box-shadow: 0 6px 18px rgba(0,0,0,.18);
  }

  /* Back side */
  .card--back {
    background: radial-gradient(ellipse at 55% 35%, var(--card-dark-mid) 0%, var(--card-dark) 70%);
    color: #ffffff;
    text-align: center;
  }
  .brand {
    display: flex; align-items: center; justify-content: center; gap: 14px;
  }
  .brand__dot {
    width: 34px; height: 34px; border-radius: 50%;
    background: var(--accent-red);
  }
  .brand__name {
    font-size: 44px; letter-spacing: 0.5px; line-height: 1;
  }
  .card--back .brand { margin-top: 92px; }
  .back-url {
    font-size: 17px; margin-top: 62px; letter-spacing: 0.3px;
  }
  .compliance {
    font-size: 9.5px; line-height: 1.45; color: var(--muted-grey);
    margin: 10px auto 0; width: 420px;
  }

  /* Front side */
  .card--front { background: var(--card-light); color: var(--ink); }
  .name-tab {
    position: absolute; left: 0; top: 28px;
    width: 250px; height: 40px;
    background: var(--tab-black);
    border-radius: 0 20px 20px 0;
    display: flex; align-items: center; justify-content: flex-end; padding-right: 14px;
  }
  .name-tab__dot { width: 20px; height: 20px; border-radius: 50%; background: var(--accent-red); }
  .person {
    position: absolute; left: 30px; top: 80px; width: 220px;
    text-align: right;
  }
  .person__name { font-family: "Arimo", Arial, sans-serif; font-weight: 700; font-size: 16px; }
  .person__title { font-size: 15px; color: var(--ink-soft); margin-top: 3px; }
  .person__role { font-size: 13px; color: var(--accent-red); margin-top: 14px; }

  .front-info { position: absolute; left: 272px; top: 84px; width: 250px; }
  .card--front .brand { justify-content: flex-start; gap: 10px; }
  .card--front .brand__dot { width: 24px; height: 24px; }
  .card--front .brand__name { font-size: 27px; color: var(--ink); }
  .address { font-size: 15px; margin-top: 18px; }
  .contacts { list-style: none; margin-top: 10px; font-size: 12.5px; }
  .contacts li { display: flex; align-items: center; gap: 8px; height: 20px; }
  .contacts svg { width: 14px; height: 14px; flex: none; }
  .icon-square { width: 14px; height: 14px; border-radius: 3px; flex: none; }
  .icon-square--twitter { background: var(--twitter-blue); }
  .icon-square--facebook { background: var(--facebook-blue); }
</style>
</head>
<body>
<main class="sheet">

  <section class="card card--back" aria-label="Card back">
    <div class="brand">
      <span class="brand__dot"></span>
      <span class="brand__name">thornal insurance</span>
    </div>
    <p class="back-url">http://www.thornalcover.example.au</p>
    <p class="compliance">Thornal Insurance Services Pty Ltd [ABN 61728405913] AR No 586027 as Authorised Representative of Carrodine Insurance Group Pty Ltd ACN 274 619 508 ABN 82 274 619 508 AFS Licence No 718246</p>
  </section>

  <section class="card card--front" aria-label="Card front">
    <div class="name-tab"><span class="name-tab__dot"></span></div>
    <div class="person">
      <p class="person__name">Dean Thornal QRTMOL</p>
      <p class="person__title">(Snr Assoc.) CIP</p>
      <p class="person__role">Director</p>
    </div>
    <div class="front-info">
      <div class="brand">
        <span class="brand__dot"></span>
        <span class="brand__name">thornal insurance</span>
      </div>
      <p class="address">PO Box 782, Fernmoor SA 5071</p>
      <ul class="contacts">
        <li>
          <svg viewBox="0 0 14 14" aria-hidden="true"><path d="M3 1h3l1 3-2 1.2a7 7 0 0 0 3.8 3.8L10 7l3 1v3c0 1-1 2-2 2C5.5 13 1 8.5 1 3c0-1 1-2 2-2z" fill="#e01f26"/></svg>
          0438 612 704 or 1300 584 619
        </li>
        <li>
          <svg viewBox="0 0 14 14" aria-hidden="true"><rect x="3" y="1" width="8" height="4" fill="none" stroke="#e01f26" stroke-width="1.2"/><rect x="1" y="5" width="12" height="6" rx="1" fill="#e01f26"/><rect x="3" y="9" width="8" height="4" fill="#fff" stroke="#e01f26" stroke-width="1.2"/></svg>
          08 8347 2910
        </li>
        <li>
          <svg viewBox="0 0 14 14" aria-hidden="true"><rect x="1" y="3" width="12" height="8" rx="1" fill="none" stroke="#777" stroke-width="1.2"/><path d="M1.5 3.5 7 8l5.5-4.5" fill="none" stroke="#777" stroke-width="1.2"/></svg>
          dean@thornalcover.example.au
        </li>
        <li><span class="icon-square icon-square--twitter"></span>Thornalcover</li>
        <li><span class="icon-square icon-square--facebook"></span>thornalcover</li>
      </ul>
    </div>
  </section>

</main>
</body>
</html>
```